Velvet Orchard - R&B Band in Sydney Requires new Business Cards

We're a 6 piece R&B Soul band in Sydney called Velvet Orchard that requires new promotional material including Business Cards.

We are very well known around Sydney and have a resident venue gig at the Marlowe Sydney hotel. We play predominantly old & new school R&B hits.

Our logo is attached, colours are Brown & yellow.
Initial idea was to get sugar packets made up with our logo and contact details.

```html
<!DOCTYPE html>
<html lang="en">
<head>
<meta charset="utf-8">
<title>Velvet Orchard – Business Cards</title>
<link rel="stylesheet" href="https://fonts.googleapis.com/css2?family=Arimo:wght@400;700&display=swap">
<style>
  :root {
    --page: #ffffff;
    --frame-brown: #5a3212;
    --panel-tan: #b27b3b;
    --panel-tan-light: #be8a47;
    --stripe-brown: #8c5a26;
    --name-brown: #3a2210;
    --accent-yellow: #ecd400;
    --web-shadow: rgba(70, 40, 10, 0.85);
    --back-orange: #f5b950;
    --back-band: #b57a36;
  }
  * { margin: 0; padding: 0; box-sizing: border-box; }
  html, body {
    width: 1200px; height: 557px; overflow: hidden;
    background: var(--page);
    font-family: "Arimo", Arial, sans-serif;
  }
  .canvas { position: relative; width: 1200px; height: 557px; }

  .card { position: absolute; top: 132px; width: 423px; height: 242px; overflow: hidden; }

  /* Front */
  .card-front { left: 139px; background: var(--frame-brown); }
  .front-panel {
    position: absolute; left: 10px; top: 10px; right: 10px; bottom: 10px;
    background: radial-gradient(ellipse at center, var(--panel-tan-light), var(--panel-tan));
    border-radius: 6px;
  }
  .front-stripe { position: absolute; left: 10px; right: 10px; height: 14px; background: var(--stripe-brown); }
  .front-stripe.s1 { top: 66px; }
  .front-stripe.s2 { top: 90px; }
  .front-stripe.s3 { top: 114px; }
  .front-name {
    position: absolute; left: 0; right: 0; top: 44px;
    text-align: center; color: var(--name-brown);
    font-weight: 700; font-size: 50px; line-height: 60px; letter-spacing: 1px;
    text-transform: uppercase;
  }
  .front-web {
    position: absolute; left: 0; right: 0; top: 181px;
    text-align: center; color: var(--accent-yellow);
    font-size: 18px; letter-spacing: 1.5px;
  }

  /* Back */
  .card-back { left: 600px; background: var(--back-orange); }
  .back-band-h { position: absolute; left: 0; top: 31px; width: 266px; height: 13px; background: var(--back-band); }
  .back-band-v { position: absolute; left: 380px; top: 124px; width: 14px; bottom: 0; background: var(--back-band); }
  .back-name {
    position: absolute; right: 16px; top: 20px; width: 140px;
    text-align: center; color: var(--name-brown);
    font-weight: 700; font-size: 26px; line-height: 32px;
    text-transform: uppercase;
  }
  .back-web {
    position: absolute; right: 12px; top: 100px; width: 175px;
    text-align: center; color: var(--accent-yellow);
    font-size: 13px; font-weight: 700; letter-spacing: 0.3px;
    text-shadow: 0 0 3px var(--web-shadow), 0 1px 1px var(--web-shadow);
  }
</style>
</head>
<body>
<main class="canvas">
  <section class="card card-front" aria-label="Business card front">
    <div class="front-panel" role="img" aria-label="Textured tan paper panel with rough torn edges"></div>
    <div class="front-stripe s1"></div>
    <div class="front-stripe s2"></div>
    <div class="front-stripe s3"></div>
    <h1 class="front-name">Velvet<br>Orchard</h1>
    <p class="front-web">velvetorchardmusic.com.au</p>
  </section>

  <section class="card card-back" aria-label="Business card back">
    <div class="back-band-h"></div>
    <div class="back-band-v"></div>
    <p class="back-name">Velvet<br>Orchard</p>
    <p class="back-web">velvetorchardmusic.com.au</p>
  </section>
</main>
</body>
</html>
```